Korean Homemade food restaurant just like what your mom cooks at home

I need a black and white simple and modern design according to my logo.
My restaurant name is Noru Kan (meaning of home cooking).
I need to have 솔찬(Noru Kan) in Korean need to be included. Once again 솔찬.
I am not sure if I need to include my name and number and adress.

솔찬 Noru Kan 418 Marlow Ct. Fernhollow, NK 37512 Grant Oh Owner Cell:555-555-0183 Store:555-555-0297

Target Market(s)

business owners, university students

Industry/Entity Type

Restaurant

Contact Information for Business Card

This is traditional Korean food restaurant that targets university students during lunch and Korean business travelers at dinner.

Font styles to use
Sans Serif

Requirements
Must have
• Must have my logo.

```html
<!DOCTYPE html>
<html lang="en">
<head>
<meta charset="utf-8">
<title>Noru Kan — Business Card</title>
<link href="https://fonts.googleapis.com/css2?family=Questrial&family=Noto+Sans+KR:wght@300&display=swap" rel="stylesheet">
<style>
  :root {
    --backdrop: #2b2b2b;
    --card: #ffffff;
    --ink: #111111;
  }
  html, body {
    margin: 0;
    padding: 0;
    width: 1200px;
    height: 900px;
    overflow: hidden;
    background: var(--backdrop);
  }
  .canvas {
    position: relative;
    width: 1200px;
    height: 900px;
    display: flex;
    align-items: center;
    justify-content: center;
  }
  .business-card {
    position: relative;
    width: 440px;
    height: 770px;
    background: var(--card);
    border-radius: 26px;
    color: var(--ink);
    font-family: "Questrial", sans-serif;
  }
  .brand {
    position: absolute;
    top: 150px;
    left: 0;
    right: 0;
    text-align: center;
  }
  .brand-mark {
    display: flex;
    align-items: center;
    justify-content: center;
    gap: 14px;
  }
  .brand-dot {
    width: 34px;
    height: 34px;
    border-radius: 50%;
    background: var(--ink);
  }
  .brand-name {
    font-size: 64px;
    line-height: 1;
    letter-spacing: -1px;
    margin: 0;
    font-weight: 400;
  }
  .brand-korean {
    display: flex;
    align-items: center;
    justify-content: center;
    gap: 18px;
    margin-top: 26px;
  }
  .brand-korean .rule {
    width: 92px;
    height: 2px;
    background: var(--ink);
  }
  .brand-korean .hangul {
    font-family: "Noto Sans KR", sans-serif;
    font-weight: 300;
    font-size: 44px;
    line-height: 1;
  }
  .contact {
    position: absolute;
    left: 92px;
    bottom: 110px;
    font-size: 19px;
    line-height: 1.55;
    letter-spacing: 0.6px;
    text-transform: uppercase;
  }
  .contact p { margin: 0; white-space: pre; }
</style>
</head>
<body>
  <main class="canvas">
    <article class="business-card">
      <header class="brand">
        <div class="brand-mark">
          <span class="brand-dot" aria-hidden="true"></span>
          <h1 class="brand-name">Noru Kan</h1>
        </div>
        <div class="brand-korean">
          <span class="rule"></span>
          <span class="hangul" lang="ko">솔찬</span>
          <span class="rule"></span>
        </div>
      </header>
      <section class="contact">
        <p>Grant Oh  -  Owner</p>
        <p>Cell:     555-555-0183</p>
        <p>Store:    555-555-0297</p>
        <p>418  Marlow  Ct.</p>
        <p>Fernhollow, NK 37512</p>
      </section>
    </article>
  </main>
</body>
</html>
```